The Drawer Sage needs a business card

The drawer sage is a lead generation service serving the Custom Closet industry.

Here is the basic card information:

The Drawer Sage
Gregory Tessman
Owner/CEO
Ashbury, NC
704-555-0183 Cell
Email: gtessman@TheDrawerSage.example

Additional information for the card:

"High quality, flat rate lead generation exclusively for the custom closet industry"

Bullet points for the back:

- Low fixed cost
- Easy to budget
- Guaranteed qualified Leeds
- Exclusivity per city

Logo attached, head shot attached. Photos of closet systems attached

```html
<!DOCTYPE html>
<html lang="en">
<head>
<meta charset="utf-8">
<title>The Drawer Sage – Business Card</title>
<link rel="stylesheet" href="https://fonts.googleapis.com/css2?family=Open+Sans:wght@400;600;800&display=swap">
<style>
  :root {
    --backdrop: #474747;
    --card: #131313;
    --copper: #b0692e;
    --ink: #ffffff;
    --photo-dark: #0d0d0f;
    --photo-suit: #26324a;
  }
  * { box-sizing: border-box; margin: 0; padding: 0; }
  html, body { width: 1200px; height: 801px; overflow: hidden; }
  body {
    background: var(--backdrop);
    font-family: "Open Sans", Arial, sans-serif;
    color: var(--ink);
    position: relative;
  }
  .card {
    position: absolute;
    width: 525px;
    height: 300px;
    background: var(--card);
    border: 2px solid var(--copper);
    border-radius: 18px;
    overflow: hidden;
    box-shadow: 0 18px 40px rgba(0,0,0,.35);
  }
  .card--front { left: 45px; top: 250px; }
  .card--back { left: 630px; top: 250px; }

  /* Front */
  .headshot {
    position: absolute;
    right: 0; top: 0;
    width: 250px; height: 300px;
    background: radial-gradient(ellipse at 55% 70%, var(--photo-suit) 0%, #1b2234 45%, var(--photo-dark) 80%);
  }
  .front-brand {
    position: absolute;
    left: 34px; top: 42px;
    font-size: 30px;
    font-weight: 600;
    color: var(--ink);
    line-height: 1.05;
  }
  .front-brand .brand-dot {
    display: inline-block;
    width: 10px; height: 10px;
    border-radius: 50%;
    background: var(--copper);
    margin-right: 8px;
    vertical-align: middle;
  }
  .edge-tab {
    position: absolute;
    left: 0; top: 150px;
    width: 14px; height: 34px;
    background: var(--copper);
  }
  .person { position: absolute; left: 34px; top: 140px; }
  .person__name {
    font-size: 24px;
    font-weight: 800;
    color: var(--copper);
    line-height: 1.1;
  }
  .person__role { font-size: 14px; margin-top: 2px; }
  .contact {
    position: absolute;
    left: 34px; top: 210px;
    list-style: none;
    font-size: 13.5px;
    line-height: 1.65;
  }
  .contact li { display: flex; align-items: center; gap: 8px; }
  .contact svg { width: 12px; height: 12px; flex: none; fill: var(--copper); }

  /* Back */
  .back-brand {
    position: absolute;
    left: 0; right: 0; top: 62px;
    text-align: center;
    font-size: 52px;
    font-weight: 600;
    color: var(--ink);
    letter-spacing: .5px;
  }
  .tagline {
    position: absolute;
    left: 0; right: 0; top: 160px;
    text-align: center;
    font-size: 13px;
  }
  .benefits {
    position: absolute;
    left: 92px; top: 196px;
    display: grid;
    grid-template-columns: auto auto;
    column-gap: 14px;
    row-gap: 4px;
    list-style: none;
    font-size: 15px;
  }
  .benefits li { display: flex; align-items: center; gap: 10px; }
  .benefits .right::before {
    content: "";
    width: 9px; height: 9px;
    border-radius: 50%;
    background: var(--copper);
    display: inline-block;
  }
</style>
</head>
<body>

<section class="card card--front" aria-label="Business card front">
  <div class="headshot" role="img" aria-label="Portrait photo of Gregory Tessman in a navy checked blazer, arms crossed"></div>
  <div class="front-brand"><span class="brand-dot"></span>The Drawer Sage</div>
  <div class="edge-tab"></div>
  <div class="person">
    <div class="person__name">Gregory Tessman</div>
    <div class="person__role">Owner/CEO</div>
  </div>
  <ul class="contact">
    <li><svg viewBox="0 0 12 12"><path d="M6 0a4 4 0 0 0-4 4c0 3 4 8 4 8s4-5 4-8a4 4 0 0 0-4-4zm0 5.5A1.5 1.5 0 1 1 6 2.5a1.5 1.5 0 0 1 0 3z"/></svg>Ashbury, NC</li>
    <li><svg viewBox="0 0 12 12"><path d="M3 0h6a1 1 0 0 1 1 1v10a1 1 0 0 1-1 1H3a1 1 0 0 1-1-1V1a1 1 0 0 1 1-1zm0 1.5v8h6v-8z"/></svg>704-555-0183</li>
    <li><svg viewBox="0 0 12 12"><path d="M0 2h12v8H0zm1 1 5 4 5-4z"/></svg>gtessman@TheDrawerSage.example</li>
  </ul>
</section>

<section class="card card--back" aria-label="Business card back">
  <div class="back-brand">The Drawer Sage</div>
  <p class="tagline">High quality, flat rate lead generation exclusively for the custom closet industry</p>
  <ul class="benefits">
    <li>Low fixed cost</li>
    <li class="right">Guaranteed qualified Leeds</li>
    <li>Easy to budget</li>
    <li class="right">Exclusivity per city</li>
  </ul>
</section>

</body>
</html>
```